Personal Injury Book Ad Photo Set

I need a series of images for a Threadloop ad campaign for promoting a book titled "Making Sense of an Accident Claim".

```html
<!DOCTYPE html>
<html lang="en">
<head>
<meta charset="utf-8">
<title>Making Sense of an Accident Claim – Book Ad</title>
<link href="https://fonts.googleapis.com/css2?family=Bebas+Neue&family=Poppins:wght@400;600;700&display=swap" rel="stylesheet">
<style>
  :root {
    --page-bg: #f7f7f8;
    --navy: #252a5f;
    --navy-soft: #8f96d6;
    --title-grey: #58585c;
    --body-grey: #6a6a6e;
    --ink: #2b2b2e;
    --panel-light: #eeeeef;
    --panel-mid: #dcdcde;
    --book-dark: #1c1c1f;
    --book-mid: #3a3a3f;
    --white: #ffffff;
  }
  * { margin: 0; padding: 0; box-sizing: border-box; }
  html, body {
    width: 800px;
    height: 1200px;
    overflow: hidden;
    background: var(--page-bg);
  }
  .canvas {
    position: relative;
    width: 800px;
    height: 1200px;
  }
  .ad-banner {
    position: absolute;
    left: 20px;
    top: 400px;
    width: 760px;
    height: 397px;
    overflow: hidden;
    background: linear-gradient(120deg, var(--white) 0%, var(--panel-light) 45%, var(--panel-mid) 100%);
    box-shadow: 8px 10px 18px rgba(0,0,0,0.18);
  }
  .backdrop-photo {
    position: absolute;
    left: 0;
    top: 0;
    width: 560px;
    height: 397px;
    background: radial-gradient(ellipse at 40% 30%, rgba(200,200,204,0.55) 0%, rgba(235,235,237,0.3) 45%, rgba(255,255,255,0) 75%);
  }
  .shape-layer {
    position: absolute;
    inset: 0;
  }
  .headline {
    position: absolute;
    left: 42px;
    top: 54px;
    width: 330px;
    font-family: "Bebas Neue", "Arial Narrow", sans-serif;
    color: var(--title-grey);
  }
  .headline-top {
    display: block;
    font-size: 66px;
    line-height: 60px;
    letter-spacing: 0.5px;
  }
  .headline-band {
    display: block;
    margin-top: 6px;
    height: 37px;
    background: var(--navy);
    color: var(--white);
    font-family: "Poppins", sans-serif;
    font-weight: 700;
    font-size: 21px;
    line-height: 37px;
    letter-spacing: 8.5px;
    text-align: center;
  }
  .headline-bottom {
    display: block;
    margin-top: 6px;
    font-size: 94px;
    line-height: 82px;
  }
  .byline {
    position: absolute;
    left: 42px;
    top: 256px;
    font-family: "Poppins", sans-serif;
    font-size: 19px;
    color: var(--body-grey);
  }
  .byline-name {
    margin-left: 8px;
    font-size: 25px;
    font-weight: 700;
    color: var(--navy);
  }
  .cta {
    position: absolute;
    left: 42px;
    top: 318px;
    display: flex;
    align-items: center;
    font-family: "Poppins", sans-serif;
  }
  .cta-label {
    font-size: 16px;
    font-weight: 600;
    color: var(--ink);
    letter-spacing: -0.3px;
  }
  .cta-label span { font-weight: 400; }
  .url-pill {
    position: relative;
    display: flex;
    align-items: center;
    margin-left: 10px;
    width: 340px;
    height: 26px;
    border-radius: 13px;
    background: linear-gradient(90deg, #6a6a6e 0%, #8b8b8f 55%, rgba(180,180,184,0) 100%);
  }
  .url-icon {
    width: 26px;
    height: 26px;
    flex: none;
  }
  .url-text {
    margin-left: 10px;
    font-size: 15px;
    font-weight: 600;
    letter-spacing: 1.2px;
    color: var(--white);
  }
  .book-stack {
    position: absolute;
    left: 430px;
    top: 36px;
    width: 250px;
    height: 320px;
    transform: rotate(14deg);
    border-radius: 3px;
    background: linear-gradient(160deg, var(--book-mid) 0%, var(--book-dark) 60%, #0f0f11 100%);
    box-shadow: 14px 24px 22px rgba(0,0,0,0.35);
  }
  .social-links {
    position: absolute;
    right: 50px;
    top: 322px;
    display: flex;
    flex-direction: column;
    gap: 2px;
    font-family: "Poppins", sans-serif;
    font-size: 11px;
    font-weight: 600;
    color: var(--navy);
  }
  .social-item {
    display: flex;
    align-items: center;
    gap: 5px;
  }
  .social-dot {
    width: 9px;
    height: 9px;
    border-radius: 50%;
    background: var(--navy);
  }
</style>
</head>
<body>
<main class="canvas">
  <section class="ad-banner">
    <div class="backdrop-photo" role="img" aria-label="Faded grey photograph of a person receiving care after an accident"></div>

    <svg class="shape-layer" width="760" height="397" viewBox="0 0 760 397" aria-hidden="true">
      <path d="M322 0 L760 0 L760 397 C730 250 620 110 322 0 Z" fill="var(--navy)"/>
      <path d="M0 351 C20 362 40 378 61 397 L0 397 Z" fill="var(--navy)"/>
    </svg>

    <h1 class="headline">
      <span class="headline-top">Making Sense</span>
      <span class="headline-band">OF AN ACCIDENT</span>
      <span class="headline-bottom">Claim</span>
    </h1>

    <p class="byline">Written By<span class="byline-name">Elias Marlow</span></p>

    <div class="cta">
      <p class="cta-label">BOOK NOW <span>at</span></p>
      <div class="url-pill">
        <svg class="url-icon" viewBox="0 0 26 26" aria-hidden="true">
          <circle cx="13" cy="13" r="12" fill="var(--navy)"/>
          <circle cx="13" cy="13" r="6" fill="none" stroke="var(--white)" stroke-width="1.5"/>
          <line x1="7" y1="13" x2="19" y2="13" stroke="var(--white)" stroke-width="1.2"/>
          <ellipse cx="13" cy="13" rx="2.6" ry="6" fill="none" stroke="var(--white)" stroke-width="1.2"/>
        </svg>
        <span class="url-text">www.marlowbooks.com</span>
      </div>
    </div>

    <div class="book-stack" role="img" aria-label="Two dark hardcover copies of the book Making Sense of an Accident Claim"></div>

    <ul class="social-links">
      <li class="social-item"><span class="social-dot"></span>Threadloop</li>
      <li class="social-item"><span class="social-dot"></span>Linkwell</li>
    </ul>
  </section>
</main>
</body>
</html>
```